Flyer for an pediatric sleep consultancy - to distribute to play and childcare centers etc.

I need a flyer that will attract the attention of parents with children between the age of babies to toddlers, who may be experiencing sleep issues. The flyer will be placed at places such as community centers, doctors room, play centers, kindergardens, etc.

My company is called "The Quiet Meadow Studio" and provides a sleep consultancy service. My service essentially provides a customized plan for parents to follow and general advice and guidance. It is not medical advice.

I like to the flyer to have an overall tone that is soft and peaceful with a clean and beautiful design, however can catch the attention of parents who may be struggling with their child's sleep issues and are sleep deprived. I would like photos with minimal text. The colour I use is a brownish rose. I will attach some of my designs to give you an idea. You can have a look at my homepage as well to get an idea about my esthetic direction and the colour. Although the colour of my page is a bit too brownish....

I will provide the text to appear in the flyer once I have a better idea of the layout that I prefer for the flyer. The text however wont be extensive, just some catchy points.

I want to direct people to my website which is www.quietmeadowstudio-example.com
I offer a first FREE evaluation call, to the parents, to get to know each other better, learn about their child's particular sleep problems and see if we are a good fit and can work together. I would like to have this information somehow on the flyer, so that the parents will contact me.
I also have a facebook page, which is: The Quiet Meadow Studio

I have a logo that I would like to appear on the flyer. I will attach the file once the uploader on art bazaar is fixed.

When I print the flyer - I like to print A5 SIZE ... please make sure the formatting is OK for this size.

Here are some text ideas. of course all of it would be too much, I guess. On the front of the flyer I would like to have some catchy phrase or something similar to get people interested and to want to know more. On the back there could be a bit more text and information. But I'm open too suggestions....
I'm not too sure about the wording yet. But here are some text that I might be use:

Is sleep an issue in your home?

Is your baby having trouble sleeping? ... are you?!
I can help!

Sleep, baby, sleep….

Teaching children how to sleep

The Quiet Meadow Studio is a pediatric sleep consultancy that specializes in helping parents with children who struggle to develop good and healthy sleep habits.
Disruptive sleep patterns or not enough sleep can affect the physical, mental and emotional development of your child.

Of course nobody plans to have a sleep problem, but habits can become easily ingrained and spiral quickly out of control and you can find yourself sleep deprived, desperate and not too sure what to do. You see all the other sleeping babies and wish there was someone who understood what you were going through?! Well, there is!

Contact me for a free 15 minute consultation.

This 15 minute „mini“ consultation is a chance to discuss your unique sleep challenges and sleep goals with me. I will provide you with an overview of how I will work with your family to achieve your wildest sleep dreams (goals).
Furthermore do I understand and believe that every child and their family is unique and there is no one size fits all!
I would love to have a chat with you and talk about how I can help make things easier for you and your family!

Do I need a sleep consultant for my child?
The answer is yes if:
- if your child will only fall asleep when nursing or bottle feeding
- if your child needs a dummy or other external aid, like being rocked, patted or taken for a care ride to fall asleep
- if your good night routine is a challenging and exhausting procedure instead of a relaxed and enjoyable moment for the whole family
- if sleep is a constant battle in your home which leaves you feeling frustrated and exhausted
- if your own lack of sleep is taking a toll on you and the whole family

What can I do for you?

I will:

- Guide you to set an age appropriate foundation for good sleep
- Create an individual sleep plan tailored especially to your child’s sleep needs and circumstances
- Help you to teach your childto go to sleep and get back to sleep independently during the night
- show you how to teach your child to take healthful, restorative naps
-Learn

Contact:

Marta Lindqvist
info@quietmeadowstudio-example.com
www.quietmeadowstudio-example.com
+34 612 380 574

Consultations in English, German or Spanish via Phone/Skype or home consultation

Reason: I have to go on a business trip and won't be able to choose a design until the deadline. During the trip I won't have time to give feedback and ask for changes. thank you

Target Market(s)

parents, sleep deprived mothers, young families, child care provider,

Industry/Entity Type

Baby Care

Contact Information for Business Card

Marta Lindqvist
pediatric sleep consultant
+34 612 380 574

```html
<!DOCTYPE html>
<html lang="en">
<head>
<meta charset="utf-8">
<title>The Quiet Meadow Studio – Flyer</title>
<link href="https://fonts.googleapis.com/css2?family=Open+Sans:ital,wght@0,300;0,400;0,600;0,700;1,600;1,700&display=swap" rel="stylesheet">
<style>
  :root{
    --rose:#f0a397;
    --rose-soft:#f4b1a7;
    --rose-deep:#e6897c;
    --rose-text:#ea8a7c;
    --ink:#5b5b5b;
    --ink-soft:#8b8b8b;
    --sage:#8e9a8e;
    --paper:#f3f2f2;
    --white:#ffffff;
    --stage:#e8e6e4;
  }
  *{box-sizing:border-box;margin:0;padding:0}
  html,body{width:1200px;height:854px;overflow:hidden}
  body{background:var(--stage);font-family:"Open Sans",Arial,sans-serif;color:var(--ink);position:relative}
  .page{position:absolute;top:72px;width:500px;height:709px;background:var(--paper);overflow:hidden;box-shadow:0 2px 8px rgba(0,0,0,.12)}
  .page--front{left:82px}
  .page--back{left:644px}
  .layer{position:absolute;left:0;top:0}

  /* brand */
  .brand{position:absolute;display:flex;align-items:center;gap:7px;font-weight:300;white-space:nowrap}
  .brand__dot{width:14px;height:14px;border-radius:50%;border:1.5px solid currentColor}
  .brand--front{right:22px;top:40px;color:var(--white);font-size:15px}
  .brand--back{left:26px;top:60px;color:var(--ink-soft);font-size:15px}

  /* clouds */
  .cloud-text{position:absolute;color:var(--white);text-align:center;font-weight:400}
  .cloud-text--small{left:18px;top:224px;width:105px;font-size:12.5px;line-height:15px}
  .cloud-text--big{left:85px;top:298px;width:200px;font-size:21px;line-height:25px}

  /* front copy */
  .headline{position:absolute;left:0;width:500px;top:371px;text-align:center;color:var(--rose-text);font-size:19px;font-weight:400}
  .subline{position:absolute;left:0;width:500px;top:400px;text-align:center;color:var(--ink-soft);font-size:16.5px;font-weight:400}
  .rule-dotted{position:absolute;left:41px;width:420px;top:438px;border-top:1.5px dotted var(--rose)}
  .column{position:absolute;top:456px;font-size:12px;line-height:13px;text-align:justify;hyphens:auto}
  .column--left{left:33px;width:200px}
  .column--right{left:264px;width:205px}
  .column__title{color:var(--rose-text);font-size:12.8px;font-weight:400;margin-bottom:12px;text-align:left}
  .column p+p{margin-top:11px}
  .column__close{color:var(--sage);font-style:italic;font-weight:700;margin-top:10px;text-align:left}

  /* footer */
  .offer{position:absolute;left:0;top:645px;width:500px;height:40px;background:var(--rose-deep);color:var(--white);text-align:center;padding-top:4px}
  .offer__title{font-weight:700;font-size:12.5px;line-height:15px}
  .offer__text{font-weight:700;font-style:italic;font-size:11px;line-height:17px}
  .contacts{position:absolute;left:0;top:685px;width:500px;height:24px;display:flex;justify-content:space-between;align-items:center;padding:0 16px;font-size:9px;color:var(--ink)}
  .contacts__item{display:flex;align-items:center;gap:4px;white-space:nowrap}
  .contacts__item svg{width:10px;height:10px;flex:none}

  /* back copy */
  .section-title{position:absolute;left:28px;top:137px;color:var(--rose-text);font-size:17.5px;font-weight:600}
  .service-list{position:absolute;left:34px;top:256px;width:212px;list-style:none;font-size:12px;line-height:13px;color:var(--ink)}
  .service-list li{position:relative;padding-left:16px;text-align:left;margin-bottom:10px}
  .service-list li::before{content:"";position:absolute;left:0;top:3px;width:8px;height:8px;border-radius:50%;background:var(--ink-soft)}
  .portrait{position:absolute;left:60px;top:468px;width:185px;height:177px;border-radius:90px 90px 0 0;background:linear-gradient(180deg,#f4f0ec 0%,#e6d5c8 45%,#b9c6d3 100%)}

  .qa{position:absolute;left:279px;top:236px;width:221px;height:367px;background:var(--rose-soft);border-radius:0 0 0 16px;padding:34px 14px 0 16px;color:var(--white)}
  .qa__title{font-size:15.5px;font-weight:700;line-height:20px}
  .qa__rule{border-top:1px solid rgba(255,255,255,.6);margin:9px 0 7px}
  .qa__lead{font-size:13.5px;font-weight:400;margin-bottom:8px}
  .qa__list{list-style:none;font-size:11px;line-height:13px}
  .qa__list li{position:relative;padding-left:12px;margin-bottom:6px}
  .qa__list li::before{content:"";position:absolute;left:1px;top:2px;width:4px;height:7px;border:solid var(--white);border-width:0 1.5px 1.5px 0;transform:rotate(40deg)}
</style>
</head>
<body>

<!-- FRONT -->
<section class="page page--front">
  <svg class="layer" width="500" height="709" viewBox="0 0 500 709">
    <defs>
      <linearGradient id="frontPhoto" x1="0" y1="0" x2="1" y2="1">
        <stop offset="0" stop-color="#efedec"/>
        <stop offset=".5" stop-color="#e2d6cf"/>
        <stop offset="1" stop-color="#f2f1f1"/>
      </linearGradient>
    </defs>
    <path d="M0 0H500V322C420 340 320 330 230 305 150 282 70 270 0 268Z" fill="url(#frontPhoto)" role="img" aria-label="Photo: a baby peeking over a white blanket"/>
    <path d="M245 0C262 62 372 88 500 84V0Z" fill="var(--rose)"/>
    <g fill="var(--rose)" stroke="var(--white)" stroke-width="6">
      <ellipse cx="70" cy="238" rx="58" ry="30"/>
      <circle cx="86" cy="212" r="28"/>
    </g>
    <g fill="var(--rose)">
      <ellipse cx="70" cy="238" rx="58" ry="30"/>
      <circle cx="86" cy="212" r="28"/>
    </g>
    <g fill="var(--rose)" stroke="var(--white)" stroke-width="6">
      <ellipse cx="180" cy="318" rx="118" ry="34"/>
      <circle cx="205" cy="262" r="48"/>
      <circle cx="112" cy="300" r="28"/>
      <circle cx="270" cy="302" r="30"/>
    </g>
    <g fill="var(--rose)">
      <ellipse cx="180" cy="318" rx="118" ry="34"/>
      <circle cx="205" cy="262" r="48"/>
      <circle cx="112" cy="300" r="28"/>
      <circle cx="270" cy="302" r="30"/>
    </g>
  </svg>

  <div class="brand brand--front"><span class="brand__dot"></span>The Quiet Meadow Studio</div>
  <div class="cloud-text cloud-text--small">Sleep, baby,<br>sleep....</div>
  <div class="cloud-text cloud-text--big">Is sleep an issue<br>in your home?</div>

  <h1 class="headline">Is your baby having trouble sleeping? ... are you?!</h1>
  <p class="subline">I CAN HELP!</p>
  <div class="rule-dotted"></div>

  <div class="column column--left">
    <h2 class="column__title">Teaching children how to sleep</h2>
    <p>The Quiet Meadow Studio is a pediatric sleep consultancy that specializes in helping parents with children who struggle to develop good and healthy sleep habits.</p>
    <p>Disruptive sleep patterns or not enough sleep can affect the physical, mental and emotional development of your child.</p>
  </div>
  <div class="column column--right">
    <p>Of course nobody plans to have a sleep problem, but habits can become easily ingrained and spiral quickly out of control and you can find yourself sleep deprived, desperate and not too sure what to do. You see all the other sleeping babies and wish there was someone who understood what you were going through?!</p>
    <p class="column__close">Well, there is!</p>
  </div>

  <div class="offer">
    <div class="offer__title">FREE EVALUATION CALL</div>
    <div class="offer__text">Contact me for a free 15 minute consultation at +34 612 380 574</div>
  </div>
  <div class="contacts">
    <span class="contacts__item"><svg viewBox="0 0 12 12"><circle cx="6" cy="6" r="5.5" fill="none" stroke="var(--rose)"/><rect x="3" y="4" width="6" height="4" fill="none" stroke="var(--rose)"/><path d="M3 4l3 2.3L9 4" fill="none" stroke="var(--rose)"/></svg>info@quietmeadowstudio-example.com</span>
    <span class="contacts__item"><svg viewBox="0 0 12 12"><circle cx="6" cy="6" r="5.5" fill="none" stroke="var(--rose)"/><path d="M4 3.2l1 1.6-.6.8c.5 1 1.2 1.7 2.1 2.1l.8-.6 1.6 1-.6 1C5.5 9 3 6.5 3.1 3.8Z" fill="var(--rose)"/></svg>+34 612 380 574</span>
    <span class="contacts__item"><svg viewBox="0 0 12 12"><circle cx="6" cy="6" r="5.5" fill="none" stroke="var(--rose)"/><circle cx="6" cy="6" r="3" fill="none" stroke="var(--rose)"/><path d="M3 6h6M6 3v6" stroke="var(--rose)" stroke-width=".7"/></svg>quietmeadowstudio-example.com</span>
  </div>
</section>

<!-- BACK -->
<section class="page page--back">
  <svg class="layer" width="500" height="709" viewBox="0 0 500 709">
    <defs>
      <linearGradient id="backPhoto" x1="0" y1="0" x2="1" y2="1">
        <stop offset="0" stop-color="#f1ebe6"/>
        <stop offset=".55" stop-color="#e8d3c6"/>
        <stop offset="1" stop-color="#f5f3f3"/>
      </linearGradient>
    </defs>
    <path d="M0 0H500V236H0Z" fill="var(--white)"/>
    <path d="M0 205C110 200 230 206 330 226 230 222 110 226 0 246V250H500V236H0Z" fill="var(--paper)"/>
    <path d="M0 178C110 164 230 172 330 208 230 186 110 184 0 200Z" fill="var(--rose)"/>
    <path d="M0 212C110 198 230 198 320 214 220 208 110 210 0 226Z" fill="#e4e2e2"/>
    <circle cx="377" cy="123" r="142" fill="var(--rose)"/>
    <circle cx="377" cy="123" r="134" fill="var(--white)"/>
    <circle cx="377" cy="123" r="128" fill="url(#backPhoto)" role="img" aria-label="Photo: two young children asleep side by side"/>
    <g fill="var(--rose-soft)">
      <ellipse cx="212" cy="200" rx="30" ry="12"/>
      <circle cx="222" cy="188" r="15"/>
      <ellipse cx="270" cy="222" rx="42" ry="18"/>
      <circle cx="280" cy="203" r="23"/>
      <circle cx="248" cy="215" r="13"/>
    </g>
  </svg>

  <div class="brand brand--back"><span class="brand__dot"></span>The Quiet Meadow Studio</div>
  <h2 class="section-title">What can I do for you?</h2>

  <ul class="service-list">
    <li>Guide you to set an age appropriate foundation for good sleep</li>
    <li>Create an individual sleep plan tailored especially to your child's sleep needs and circumstances</li>
    <li>Help you to teach your child to go to sleep and get back to sleep independently during the night</li>
    <li>Show you how to teach your child to take healthful, restorative naps</li>
    <li>Learn</li>
  </ul>

  <div class="portrait" role="img" aria-label="Photo: the sleep consultant holding a toddler"></div>

  <div class="qa">
    <h3 class="qa__title">Do I need a sleep consultant for my child?</h3>
    <div class="qa__rule"></div>
    <p class="qa__lead">The answer is YES if:</p>
    <ul class="qa__list">
      <li>if your child will only fall asleep when nursing or bottle feeding</li>
      <li>if your child needs a dummy or other external aid, like being rocked, patted or taken for a care ride to fall asleep</li>
      <li>if your good night routine is a challenging and exhausting procedure instead of a relaxed and enjoyable moment for the whole family</li>
      <li>if sleep is a constant battle in your home which leaves you feeling frustrated and exhausted</li>
      <li>if your own lack of sleep is taking a toll on you and the whole family</li>
    </ul>
  </div>

  <div class="offer">
    <div class="offer__title">FREE EVALUATION CALL</div>
    <div class="offer__text">Contact me for a free 15 minute consultation at +34 612 380 574</div>
  </div>
  <div class="contacts">
    <span class="contacts__item"><svg viewBox="0 0 12 12"><circle cx="6" cy="6" r="5.5" fill="none" stroke="var(--rose)"/><rect x="3" y="4" width="6" height="4" fill="none" stroke="var(--rose)"/><path d="M3 4l3 2.3L9 4" fill="none" stroke="var(--rose)"/></svg>info@quietmeadowstudio-example.com</span>
    <span class="contacts__item"><svg viewBox="0 0 12 12"><circle cx="6" cy="6" r="5.5" fill="none" stroke="var(--rose)"/><path d="M4 3.2l1 1.6-.6.8c.5 1 1.2 1.7 2.1 2.1l.8-.6 1.6 1-.6 1C5.5 9 3 6.5 3.1 3.8Z" fill="var(--rose)"/></svg>+34 612 380 574</span>
    <span class="contacts__item"><svg viewBox="0 0 12 12"><circle cx="6" cy="6" r="5.5" fill="none" stroke="var(--rose)"/><circle cx="6" cy="6" r="3" fill="none" stroke="var(--rose)"/><path d="M3 6h6M6 3v6" stroke="var(--rose)" stroke-width=".7"/></svg>quietmeadowstudio-example.com</span>
  </div>
</section>

</body>
</html>
```